Psychiatric Office Needs a Website- 1st Time Ever!

Been in practice since 2003 with no website, but finally ready to dive in. We are Maplecrest Behavioral Healthcare, a mental health outpatient practice based in Fayetteville, Georgia that sees diverse individuals and families from childhood to advanced age for a variety of conditions. We've grown by word of mouth and referral but would now like to have a digital footprint. Be the pioneer of our website and we will be sure to share. We would like to see designs that are modern, animated, fairly colorful, easy to read, and caters to all ages. Also, we would like the design to take the whole page (not be centered) and can be viewed well on phone/tablet. Please see our outline for more information. Our motto/slogan is: Maplecrest Behavioral Healthcare- A step forward in your wellness journey, so the design should try to reflect that.
Updates

Target Market(s)

Children through elderly

Industry/Entity Type

Medical

Logo Text

Stepping forward in your wellness journey

Number of Pages Required

1 page

Colors

Designer to choose colors to be used in the design.

Requirements
Must have
• Animation or moving pictures.
• Color.
• Concise.
• User friendly
• Diversity in the stock photos

```html
<!DOCTYPE html>
<html lang="en">
<head>
<meta charset="utf-8">
<title>Maplecrest Behavioral Healthcare</title>
<link rel="stylesheet" href="https://fonts.googleapis.com/css2?family=Open+Sans:wght@300;400;600;700&display=swap">
<style>
:root{
  --brand:#1e9fdc;
  --brand-light:#4fbde9;
  --ink:#1d1d1d;
  --muted:#8a8a8a;
  --body:#555;
  --bg-services:#f2f2f3;
  --bg-vision:#e8e8ea;
  --bg-faq:#ececee;
  --footer:#333335;
  --white:#fff;
  --btn-dark:#3a3a3a;
}
*{box-sizing:border-box;margin:0;padding:0}
html,body{width:1200px;height:2769px;overflow:hidden}
body{font-family:"Open Sans",Arial,sans-serif;color:var(--ink);position:relative;background:var(--white)}
.abs{position:absolute}
section,footer,header{position:absolute;left:0;width:1200px}

/* hero */
.hero{top:0;height:642px;overflow:hidden}
.hero-photo{position:absolute;inset:0;background:
  radial-gradient(ellipse 420px 300px at 560px 250px,#f6d79c 0%,#e3b77f 30%,rgba(170,140,120,0) 75%),
  linear-gradient(180deg,#7d8a99 0%,#a49a8f 35%,#b58d63 62%,#3e3126 82%,#231b15 100%)}
.brand{left:140px;top:18px;display:flex;align-items:center;gap:12px}
.brand-mark{width:40px;height:40px;border-radius:50%;background:var(--brand);border:3px solid var(--white)}
.brand-name{font-size:15px;font-weight:700;color:var(--white);width:170px;line-height:1.25}
.topbar{right:126px;top:19px;display:flex;gap:28px;font-size:11px;color:var(--white)}
.topbar span{display:flex;align-items:center;gap:7px}
.nav{right:126px;top:55px;display:flex;gap:26px;font-size:11px;font-weight:700;color:var(--white);text-transform:uppercase}
.nav a{color:inherit;text-decoration:none;padding:4px 7px}
.nav a.active{background:var(--white);color:var(--ink)}
.hero-title{left:218px;top:205px;width:420px;font-size:29px;font-weight:300;line-height:1.4;color:var(--white)}
.btn-screen{left:220px;top:367px;width:205px;height:48px;background:var(--brand-light);border:2px solid var(--white);color:var(--white);font-size:15px;font-weight:700;display:flex;align-items:center;justify-content:center;text-transform:uppercase}
.dots{display:flex;gap:11px}
.dots i{width:8px;height:8px;border-radius:50%;background:var(--white);display:block}
.dots i.on{background:var(--brand)}
.hero .dots{left:552px;top:595px}

.section-title{position:absolute;left:0;width:1200px;text-align:center;color:var(--brand);font-size:21px;font-weight:700}
.section-title::after{content:"";display:block;width:30px;height:3px;background:var(--brand);margin:14px auto 0}

/* services */
.services{top:642px;height:429px;background:var(--bg-services)}
.service{position:absolute;top:163px;width:180px;margin-left:-90px;text-align:center;font-size:12px;color:#444;line-height:1.45}
.service .icon{width:144px;height:144px;border-radius:50%;background:var(--brand);margin:0 auto 18px;display:flex;align-items:center;justify-content:center}

/* vision */
.vision{top:1071px;height:422px;background:var(--bg-vision)}
.vision h2{left:133px;top:54px;font-size:21px;font-weight:700;color:var(--brand)}
.vision h2::after{content:"";display:block;width:62px;height:3px;background:var(--brand);margin-top:6px}
.vision h3{font-size:14px;font-weight:700;color:#333}
.vision p{font-size:13px;color:var(--muted);line-height:1.5;margin-top:14px}
.vision .block{left:133px;width:490px}
.btn-more{left:134px;top:342px;width:96px;height:30px;background:var(--btn-dark);color:var(--white);font-size:10px;font-weight:700;display:flex;align-items:center;justify-content:center;text-transform:uppercase}
.vision-badge{left:782px;top:21px;width:282px;height:282px;border-radius:50%;background:var(--white)}

/* news */
.news{top:1493px;height:576px;background:var(--white)}
.news-card{position:absolute;top:150px;width:295px}
.news-photo{width:295px;height:287px}
.news-date{font-size:9px;font-weight:600;margin:18px 0 0 18px}
.news-card h4{font-size:13px;font-weight:700;margin:5px 0 0 18px;text-transform:uppercase}
.news-card p{font-size:12px;color:#444;margin:4px 0 0 18px;width:200px;line-height:1.35}
.arrow{top:277px}

/* faq */
.faq{top:2069px;height:349px;background:var(--bg-faq)}
.faq-card{position:absolute;top:128px;width:220px;height:131px;background:var(--white);padding:24px 26px}
.faq-card h4{font-size:12px;font-weight:600;line-height:1.4}
.faq-card p{font-size:12px;color:#444;line-height:1.4;margin-top:10px}
.faq .dots{left:570px;top:300px}
.faq .dots i{width:6px;height:6px;background:#bbb}
.faq .dots i.on{background:var(--brand)}

/* footer */
.site-footer{top:2418px;height:351px;background:var(--footer);color:var(--white)}
.foot-brand{left:128px;top:50px;width:154px;height:154px;border-radius:50%;background:var(--brand);border:4px solid var(--white);display:flex;align-items:center;justify-content:center;text-align:center;font-size:14px;font-weight:700;line-height:1.3;padding:18px}
.foot-col h5{font-size:11px;font-weight:600;text-transform:uppercase;margin-bottom:22px}
.foot-col li{list-style:none;font-size:12px;line-height:1.45}
.contact li{display:flex;gap:16px;margin-bottom:18px;line-height:1.5}
.contact svg{flex:none;margin-top:3px}
.email-field{width:257px;height:37px;background:var(--white);color:#333;font-size:12px;padding:10px 14px}
.btn-sign{margin-top:18px;width:95px;height:35px;background:var(--brand-light);font-size:12px;font-weight:700;display:flex;align-items:center;justify-content:center;text-transform:uppercase}
.foot-rule{left:133px;top:255px;width:934px;height:1px;background:#555}
.follow{left:133px;top:298px;display:flex;align-items:center;gap:12px;font-size:11px;font-weight:700;text-transform:uppercase}
.follow i{width:28px;height:28px;border-radius:50%;background:#3c5fb4;display:block}
.copyright{right:133px;top:305px;font-size:11px}
</style>
</head>
<body>

<header class="hero">
  <div class="hero-photo" role="img" aria-label="Photo of a woman with raised arms in a meadow at sunset"></div>
  <div class="abs brand"><span class="brand-mark"></span><span class="brand-name">Maplecrest Behavioral Healthcare</span></div>
  <div class="abs topbar">
    <span><svg width="10" height="10" viewBox="0 0 10 10"><circle cx="5" cy="5" r="4" fill="none" stroke="#fff" stroke-width="1.3"/><path d="M5 2.5V5h2" stroke="#fff" stroke-width="1.2" fill="none"/></svg>M-F : 9.00 AM - 9.00PM</span>
    <span><svg width="10" height="10" viewBox="0 0 10 10"><path d="M2 1l2 2-1 1.5a6 6 0 0 0 2.5 2.5L7 6l2 2-1.5 1.5C4.5 9 1 5.5.5 2.5z" fill="#fff"/></svg>770.555.0142</span>
    <span><svg width="10" height="10" viewBox="0 0 10 10"><circle cx="5" cy="3" r="2.3" fill="#fff"/><path d="M1 10c0-3 2-4 4-4s4 1 4 4z" fill="#fff"/></svg>PATIENT PORTAL</span>
  </div>
  <nav class="abs nav"><a class="active">Home</a><a>About us</a><a>Services</a><a>Conditions we treat</a><a>New patients</a></nav>
  <h1 class="abs hero-title">Maplecrest Behavioral Healthcare- A step forward in your wellness journey</h1>
  <div class="abs btn-screen">Take a screening</div>
  <div class="abs dots"><i></i><i></i><i class="on"></i><i></i><i></i></div>
</header>

<section class="services">
  <h2 class="section-title" style="top:65px">Our Services</h2>
  <div class="service" style="left:170px"><div class="icon"><svg width="64" height="64" viewBox="0 0 64 64" fill="none" stroke="#fff" stroke-width="3"><path d="M16 8v18a12 12 0 0 0 24 0V8"/><path d="M28 38v8a10 10 0 0 0 20 0v-6"/><circle cx="48" cy="34" r="5"/></svg></div>Diagnostic Evaluation<br>and Treatment</div>
  <div class="service" style="left:343px"><div class="icon"><svg width="64" height="64" viewBox="0 0 64 64" fill="none" stroke="#fff" stroke-width="3"><rect x="14" y="24" width="36" height="16" rx="8" transform="rotate(-35 32 32)"/><path d="M27 21l10 22"/></svg></div>Psychopharmacology</div>
  <div class="service" style="left:526px"><div class="icon"><svg width="64" height="64" viewBox="0 0 64 64" fill="#fff"><rect x="30" y="10" width="14" height="22" rx="2" transform="rotate(45 37 21)"/><rect x="14" y="32" width="5" height="28" rx="2" transform="rotate(45 16 46)"/></svg></div>Bariatric pre-surgical<br>consultation</div>
  <div class="service" style="left:702px"><div class="icon"><svg width="64" height="64" viewBox="0 0 64 64" fill="none" stroke="#fff" stroke-width="3"><circle cx="28" cy="40" r="13"/><path d="M20 12v18h20l6 14h6"/></svg></div>Disability and<br>work-related reportS</div>
  <div class="service" style="left:875px"><div class="icon"><svg width="64" height="64" viewBox="0 0 64 64" fill="none" stroke="#fff" stroke-width="3"><rect x="16" y="12" width="32" height="42" rx="3"/><path d="M24 26h16M24 34h16M24 42h10"/></svg></div>Early childhood<br>Assessments</div>
  <div class="service" style="left:1045px"><div class="icon"><svg width="64" height="64" viewBox="0 0 64 64" fill="#fff"><path d="M32 52C18 42 10 34 10 24a11 11 0 0 1 22-3 11 11 0 0 1 22 3c0 10-8 18-22 28z"/></svg></div>Substance abuse<br>assessments</div>
</section>

<section class="vision">
  <h2 class="abs">Vision &amp; Mission</h2>
  <div class="abs block" style="top:134px"><h3>Vision</h3><p>To be the leading provider of outpatient psychiatric care in Atlanta Metro South, working together to promote (the) mental wellness of our community</p></div>
  <div class="abs block" style="top:226px"><h3>Mission</h3><p>To provide mental health services to children, adults, and the developmentally disabled population that is culturally sensitive regardless of age, race, gender, orientation, religion, or creed;</p></div>
  <div class="abs btn-more">Read more</div>
  <div class="abs vision-badge"></div>
</section>

<section class="news">
  <h2 class="section-title" style="top:52px">News &amp; Events</h2>
  <svg class="abs arrow" style="left:66px" width="20" height="34" viewBox="0 0 20 34"><path d="M16 3L4 17l12 14" fill="none" stroke="#999" stroke-width="3"/></svg>
  <svg class="abs arrow" style="left:1100px" width="20" height="34" viewBox="0 0 20 34"><path d="M4 3l12 14L4 31" fill="none" stroke="#999" stroke-width="3"/></svg>
  <article class="news-card" style="left:133px"><div class="news-photo" role="img" aria-label="Photo of a digital brain graphic held in hand" style="background:linear-gradient(135deg,#2a3442,#4b5e78 55%,#8aa0b8)"></div><div class="news-date">SEP 20,2017</div><h4>Lorem ipsum is simply dummy</h4><p>There are many variations of pass ages of Lorem</p></article>
  <article class="news-card" style="left:451px"><div class="news-photo" role="img" aria-label="Photo of a doctor holding medicine boxes" style="background:linear-gradient(135deg,#dfe5ea,#c7d3dc 50%,#9fb3c2)"></div><div class="news-date">SEP 20,2017</div><h4>Lorem ipsum is simply dummy</h4><p>There are many variations of pass ages of Lorem</p></article>
  <article class="news-card" style="left:771px"><div class="news-photo" role="img" aria-label="Photo of a doctor talking with an older patient" style="background:linear-gradient(135deg,#e8eef0,#c9d6dc 50%,#8fa8b8)"></div><div class="news-date">SEP 20,2017</div><h4>Lorem ipsum is simply dummy</h4><p>There are many variations of pass ages of Lorem</p></article>
</section>

<section class="faq">
  <h2 class="section-title" style="top:45px">FAQ</h2>
  <div class="faq-card" style="left:133px"><h4>What do I need to bring with me to my first visit?</h4><p>Insurance card, patient forms found on our</p></div>
  <div class="faq-card" style="left:371px"><h4>How long do I have to wait to be seen?</h4><p>We try to have very little wait time for your convenience.</p></div>
  <div class="faq-card" style="left:612px"><h4>What typs of insurance do you accept?</h4><p>We accept a large variety of insurance plans.</p></div>
  <div class="faq-card" style="left:848px"><h4>Why is my child not doing well in school?</h4><p>Your child may need some testing</p></div>
  <div class="abs dots"><i></i><i></i><i class="on"></i><i></i><i></i></div>
</section>

<footer class="site-footer">
  <div class="abs foot-brand">Maplecrest Behavioral Healthcare</div>
  <div class="abs foot-col contact" style="left:340px;top:58px">
    <h5>Contact us</h5>
    <ul>
      <li><svg width="10" height="12" viewBox="0 0 10 12"><path d="M5 0a4 4 0 0 1 4 4c0 3-4 8-4 8S1 7 1 4a4 4 0 0 1 4-4z" fill="#fff"/><circle cx="5" cy="4" r="1.5" fill="#333"/></svg><span>482 Willow Bend Road<br>Fayetteville, GA 30214</span></li>
      <li><svg width="11" height="11" viewBox="0 0 10 10"><path d="M2 1l2 2-1 1.5a6 6 0 0 0 2.5 2.5L7 6l2 2-1.5 1.5C4.5 9 1 5.5.5 2.5z" fill="#fff"/></svg><span>770.555.0142</span></li>
      <li><svg width="12" height="9" viewBox="0 0 12 9"><rect width="12" height="9" rx="1" fill="#fff"/><path d="M0 1l6 4 6-4" stroke="#333" fill="none"/></svg><span>hello@maplecrestbh.com</span></li>
    </ul>
  </div>
  <div class="abs foot-col" style="left:604px;top:58px">
    <h5>Menu</h5>
    <ul><li>Home</li><li>About us</li><li>Services</li><li>Conditions We Treat</li><li>New Patients</li><li>Contact us</li></ul>
  </div>
  <div class="abs foot-col" style="left:810px;top:58px">
    <h5>Newsletter</h5>
    <div class="email-field">E mail id</div>
    <div class="btn-sign">Signup</div>
  </div>
  <div class="abs foot-rule"></div>
  <div class="abs follow">Follow us on <i></i></div>
  <div class="abs copyright">Copyrights @ 2017 All Rights Reserved</div>
</footer>

</body>
</html>
```